Frostwell Supply - Liquid Nitrogen Business Flyer

I would like a flyer for a direct mailing campaign. The target audience is strictly professional (doctors) and will be mailed to their place of business.
My company (Frostwell Supply) sells and delivers medical liquid nitrogen along with renting accessories that has to do with liquid nitrogen.

The main company is Frostwell Supply; however, Polarvane Holdings (one of the logos are attached) is its parent company and I would like it included in a small way. Around Polarvane Holdings logo - ESTABLISHED 1963

Components of the flyer:

FIRST FILL FREE

Prices are flat rate (no hidden fees... hazmat, delivery, etc.)

-Guarantee -
Will beat any competitor’s price

------Route based services ------
Set-up once and we do the rest
Peace of mind knowing you will have product

----Equipment Rentals----
Dewars-Stands-Cryoguns-Withdrawal Systems

Include ------
Company Name

(555) 382-7164

email address

Some things can be re-worded or left off, your option.. You can ask me questions anytime if any questions arise. If you come up with a "slogan” and use it on the flyer, feel free

Thank you.

Target Market(s)

Dermatologist and Family Doctors

Industry/Entity Type

Business

Colors
f37122
add136
e34297
0255a3

Requirements
Must have
• Catch the mangers eye and relay a positive message very quickly
• Be bright, colorful and CLASSY
• Have 2 sides
• Catchy and smart and abstract WILL win
Nice to have
• The flyer needs to be editable to plug in my information and any changes that might come. I work on Corel Draw X6 for editing.
• 3.74" x 8.27" LONG

```html
<!DOCTYPE html>
<html lang="en">
<head>
<meta charset="utf-8">
<title>Frostwell Supply – Rack Card</title>
<link href="https://fonts.googleapis.com/css2?family=Open+Sans:wght@400;600;700&display=swap" rel="stylesheet">
<style>
  :root {
    --orange: #f37122;
    --green: #add136;
    --pink: #e34297;
    --blue: #0255a3;
    --sky: #5aa9e6;
    --white: #ffffff;
    --ink: #2f3a1a;
    --stage: #e6e7ea;
  }
  * { margin: 0; padding: 0; box-sizing: border-box; }
  html, body { width: 900px; height: 1200px; overflow: hidden; }
  body {
    background: var(--stage);
    font-family: "Open Sans", Arial, sans-serif;
    position: relative;
  }
  .rack-card {
    position: absolute;
    left: 192px; top: 30px;
    width: 516px; height: 1140px;
    overflow: hidden;
    background: var(--orange);
    box-shadow: 0 6px 24px rgba(0,0,0,.18);
  }
  .card-shapes { position: absolute; inset: 0; }
  .brand-name {
    position: absolute; left: 28px; top: 28px;
    font-size: 26px; font-weight: 700; color: var(--blue);
    letter-spacing: .5px;
  }
  .photo-lab {
    position: absolute; left: 238px; top: 62px;
    width: 268px; height: 268px; border-radius: 50%;
    background: radial-gradient(circle at 40% 40%, #eef3f7, #aab8c4 60%, #6f7f8c);
    border: 6px solid var(--white);
    box-shadow: 0 0 0 3px var(--blue);
  }
  .photo-tubes {
    position: absolute; left: 22px; top: 215px;
    width: 252px; height: 150px; border-radius: 10px;
    background: linear-gradient(135deg, #1d6fc4, #49a5e8 55%, #0b3f7c);
    transform: rotate(-7deg);
    border: 4px solid var(--white);
  }
  .offer-pill {
    position: absolute; left: 138px; top: 474px;
    width: 270px; height: 44px; border-radius: 22px;
    background: var(--pink); color: var(--white);
    font-size: 23px; font-weight: 600; letter-spacing: .5px;
    display: flex; align-items: center; justify-content: center;
  }
  .pricing-note {
    position: absolute; left: 40px; top: 545px; width: 450px;
    color: var(--white); font-size: 24px; line-height: 1.35;
  }
  .services-box {
    position: absolute; left: 40px; top: 655px;
    width: 446px; height: 236px; border-radius: 18px;
    background: var(--green);
    padding: 18px 22px; color: var(--ink);
    font-size: 16px; line-height: 1.3;
  }
  .services-box p { margin-bottom: 10px; }
  .service-label { color: var(--pink); font-weight: 700; }
  .service-label.large { font-size: 22px; }
  .parent-name {
    position: absolute; left: 70px; top: 985px;
    font-size: 15px; font-weight: 700; color: var(--blue);
  }
  .phone-line {
    position: absolute; left: 48px; top: 1040px;
    display: flex; align-items: center; gap: 10px;
    color: var(--pink); font-size: 29px; font-weight: 600;
  }
  .illustration-doctor {
    position: absolute; left: 345px; top: 880px;
    width: 160px; height: 220px;
    border-radius: 45% 55% 40% 60% / 40% 45% 55% 60%;
    background: linear-gradient(160deg, #f27bbd, var(--pink));
    opacity: .9;
  }
</style>
</head>
<body>
  <div class="rack-card">
    <svg class="card-shapes" viewBox="0 0 516 1140" width="516" height="1140" aria-hidden="true">
      <path d="M0 0 H516 V330 C430 360 300 420 0 462 Z" fill="#ffffff"/>
      <path d="M0 450 C180 420 360 360 516 318" fill="none" stroke="#0255a3" stroke-width="22"/>
      <path d="M0 476 C190 446 360 392 516 350" fill="none" stroke="#5aa9e6" stroke-width="6"/>
      <path d="M0 1140 V935 C150 885 330 865 516 905 V1140 Z" fill="#ffffff"/>
      <path d="M0 925 C150 875 330 855 516 895" fill="none" stroke="#0255a3" stroke-width="16"/>
      <path d="M0 945 C150 898 330 878 516 915" fill="none" stroke="#5aa9e6" stroke-width="5"/>
    </svg>

    <div class="brand-name">Frostwell Supply</div>

    <div class="photo-tubes" role="img" aria-label="Photo of cryogenic sample tubes in a blue rack"></div>
    <div class="photo-lab" role="img" aria-label="Photo of a liquid nitrogen dewar and lab sample vials"></div>

    <div class="offer-pill">FIRST FILL FREE</div>

    <p class="pricing-note">Prices are flat rate (no hidden fees... hazmat, delivery, etc.)</p>

    <div class="services-box">
      <p><span class="service-label">Guarantee</span> - Will beat any competitor's price</p>
      <p><span class="service-label large">Route based services -</span><br>Set-up once and we do the rest<br>Peace of mind knowing you will have product</p>
      <p><span class="service-label">Equipment Rentals</span> - Dewars-Stands-Cryoguns-Withdrawal Systems</p>
    </div>

    <div class="illustration-doctor" role="img" aria-label="Pink splash illustration of a professional carrying supplies"></div>

    <div class="parent-name">Polarvane Holdings</div>

    <div class="phone-line">
      <svg width="30" height="30" viewBox="0 0 24 24" aria-hidden="true">
        <path fill="#e34297" d="M6.6 10.8a15.1 15.1 0 0 0 6.6 6.6l2.2-2.2a1 1 0 0 1 1-.25 11.4 11.4 0 0 0 3.6.57 1 1 0 0 1 1 1V20a1 1 0 0 1-1 1A17 17 0 0 1 3 4a1 1 0 0 1 1-1h3.5a1 1 0 0 1 1 1c0 1.25.2 2.45.57 3.57a1 1 0 0 1-.25 1z"/>
      </svg>
      <span>(555) 382-7164</span>
    </div>
  </div>
</body>
</html>
```